Nolvik Imaging Center web design and code

We need a new website for a Diagnostic Imaging Center in Fort Lauderdale, Florida.
The center has new RO advanced diagnostic equipment including a 3.0 Tesla MRI, a 128 slice PET/CT and a Varen T4 Ultrasound. Our facility has just been renovated and we have a lot of images, both facility and modality to use.
We have two client types, doctors who send their patients to our clinical Nolvik Center division, and clients who self-refer for screening studies to our Wellspire division. Both logos are attached. Please use the colors in the logos for the layout. Site should be coded in conventional HTML with CSS, but support multiple devices.
Updates

Reason: Waiting for additional designs. Most of the current designs are very similar in their structure and we would like more variety in terms of layout.

Target Market(s)

Doctors who refer patients for MRI, CT, PET, Bone Density and Ultrasound scans,
and
Retail clients who want full-body screening using MRI.

Industry/Entity Type

Medical Imaging

Coding

Coded - Design and coding required

Number of Pages Required

5+ page

Font styles to use
Sans Serif
Other font styles liked:
• Arquitecta

Requirements
Must have
• A good balance between color, shape, message and people/machine images.
• Must have images of the various machines, (RO Quillmark TN480, RO Quillmark 370, RO Varen T4) happy patients, clinical people, facility images and information about scans, preparations, costs, insurances we take.
• Must have links for social media and dynamic imagery.
Nice to have
• Some interactivity would be nice, including contact forms and scheduling application, Location map, directions, downloadable forms, history.
Should not have
• We do not want this to be built on WordPress platform. Should not be bound to a database platform that is proprietary or difficult to move.

```html
<!DOCTYPE html>
<html lang="en">
<head>
<meta charset="utf-8">
<title>Nolvik Imaging Center</title>
<link rel="stylesheet" href="https://fonts.googleapis.com/css2?family=Open+Sans:wght@400;600;700;800&display=swap">
<style>
:root{
  --green:#8dc63f;
  --green-dark:#76ab2c;
  --nav:#3d3d3d;
  --ink:#333333;
  --muted:#7a7a7a;
  --line:#e2e2e2;
  --panel:#efefef;
  --footer:#4a4a4a;
  --footer-deep:#3a3a3a;
  --white:#ffffff;
}
*{box-sizing:border-box;margin:0;padding:0}
html,body{width:1200px;height:2388px;overflow:hidden}
body{font-family:"Open Sans",Arial,sans-serif;color:var(--ink);background:var(--white);font-size:13px;line-height:1.6;position:relative}
.wrap{width:1000px;margin:0 auto;position:relative}

/* header */
.site-header{height:60px}
.site-header .wrap{height:60px;display:flex;align-items:center;justify-content:space-between}
.brand{display:flex;align-items:center;gap:10px}
.brand-mark{width:26px;height:26px;border-radius:50%;background:var(--green)}
.brand-name{font-weight:700;font-size:18px;color:var(--nav);line-height:1.05;width:150px}
.search{width:150px;height:24px;border:1px solid var(--line);font-size:10px;color:#aaa;padding:4px 8px;position:relative}
.search svg{position:absolute;right:6px;top:6px}

/* nav */
.main-nav{background:var(--nav);height:28px}
.main-nav ul{list-style:none;display:flex;width:1000px;margin:0 auto;justify-content:space-between}
.main-nav li{color:var(--white);font-size:10px;font-weight:600;letter-spacing:.5px;height:28px;line-height:28px;padding:0 24px}
.main-nav li.active{background:var(--green)}

/* hero */
.hero{position:relative;height:732px;background:linear-gradient(120deg,#d6dde3 0%,#bfc9d2 35%,#8f9ba6 60%,#c9d0d6 100%)}
.hero-shade{position:absolute;inset:0;background:rgba(40,50,60,.25)}
.hero-copy{position:absolute;left:0;right:0;top:300px;text-align:center;color:var(--white)}
.hero-copy h1{font-size:38px;font-weight:800;letter-spacing:1px}
.hero-copy p{width:620px;margin:14px auto 0;font-size:12px;line-height:1.7}
.btn{display:inline-block;background:var(--green);color:var(--white);font-weight:700;font-size:11px;letter-spacing:.5px;padding:12px 30px}
.hero-copy .btn{margin-top:40px}
.hero-arrow{position:absolute;top:388px}
.hero-arrow.prev{left:14px}
.hero-arrow.next{right:14px}

/* why */
.why{height:560px;padding-top:130px;text-align:center}
.section-title{font-size:22px;font-weight:800;color:var(--nav);letter-spacing:.3px}
.why .lead{width:720px;margin:16px auto 0;font-size:11px;color:var(--muted);line-height:1.8}
.cards{display:flex;justify-content:space-between;margin-top:40px;text-align:left}
.card{width:232px}
.card-img{height:150px;border:4px solid var(--white);box-shadow:0 0 0 1px var(--line)}
.card h3{font-size:11px;font-weight:700;margin-top:12px;color:var(--nav)}
.card p{font-size:10px;color:var(--muted);line-height:1.5;margin-top:4px}
.read-more{display:block;font-size:9px;font-weight:700;color:var(--green);margin-top:8px}

/* divisions */
.divisions{height:230px}
.divisions .wrap{display:flex;justify-content:space-between}
.division{width:480px}
.division-band{height:62px;display:flex;align-items:center;padding-left:14px;gap:8px}
.division.clinical .division-band{background:#d9d9d9}
.division.wellspire .division-band{background:var(--green)}
.division-band .dot{width:20px;height:20px;border-radius:50%}
.clinical .dot{background:var(--green)}
.wellspire .dot{background:var(--white)}
.division-band span{font-weight:700;font-size:16px;line-height:1.05;width:140px}
.clinical .division-band span{color:var(--nav)}
.wellspire .division-band span{color:var(--white)}
.division-body{background:var(--panel);height:150px;padding:16px 18px}
.division h2{font-size:15px;font-weight:800;color:var(--green-dark)}
.division p{font-size:10px;color:var(--muted);margin-top:8px;line-height:1.6}
.division .read-more{margin-top:10px}

/* wellspire */
.feature{height:380px;border-top:12px solid #d9d9d9;padding-top:36px}
.feature .section-title{text-align:left}
.feature-row{display:flex;justify-content:space-between;margin-top:20px}
.feature-text{width:480px;font-size:11px;color:var(--muted);line-height:1.8}
.feature-text p+p{margin-top:14px}
.feature-img{width:420px;height:210px;background:linear-gradient(135deg,#1d3a5c,#3f6f95 55%,#d9e3ea)}

/* footer */
.site-footer{position:absolute;left:0;top:2032px;width:1200px;height:356px;background:var(--footer);color:#d0d0d0}
.footer-cols{display:flex;justify-content:space-between;padding-top:40px}
.footer-col{width:220px;font-size:10px;line-height:1.7}
.footer-col h4{color:var(--white);font-size:14px;font-weight:600;margin-bottom:14px}
.hours{border-collapse:collapse;font-size:10px}
.hours td{padding:3px 12px 3px 0;border-bottom:1px solid #5c5c5c}
.field{width:150px;height:22px;background:#5c5c5c;margin-top:12px;font-size:9px;padding:4px 8px;color:#aaa}
.footer-col .btn{font-size:9px;padding:7px 16px;margin-top:12px}
.contact-line{display:flex;align-items:center;gap:8px;margin-bottom:6px}
.social{display:flex;gap:10px;margin-top:12px}
.social i{width:14px;height:14px;border-radius:50%;background:#d0d0d0;display:block}
.footer-bottom{position:absolute;left:0;right:0;bottom:0;height:80px;background:var(--footer-deep);font-size:10px}
.footer-bottom .wrap{padding-top:20px;line-height:1.7}
</style>
</head>
<body>

<header class="site-header">
  <div class="wrap">
    <div class="brand"><span class="brand-mark"></span><span class="brand-name">Nolvik Imaging Center</span></div>
    <div class="search">Search
      <svg width="10" height="10" viewBox="0 0 10 10"><circle cx="4" cy="4" r="3" fill="none" stroke="#999" stroke-width="1.2"/><line x1="6.2" y1="6.2" x2="9" y2="9" stroke="#999" stroke-width="1.2"/></svg>
    </div>
  </div>
</header>

<nav class="main-nav">
  <ul>
    <li class="active">HOME</li><li>ABOUT</li><li>EXAMS</li><li>WELLSPIRE</li><li>INSURANCE</li><li>SCHEDULE</li><li>CONTACT</li>
  </ul>
</nav>

<section class="hero">
  <div role="img" aria-label="Nurse smiling with a patient lying on an MRI scanner table" style="position:absolute;inset:0"></div>
  <div class="hero-shade"></div>
  <svg class="hero-arrow prev" width="14" height="22" viewBox="0 0 14 22"><polyline points="11,2 3,11 11,20" fill="none" stroke="#fff" stroke-width="3"/></svg>
  <svg class="hero-arrow next" width="14" height="22" viewBox="0 0 14 22"><polyline points="3,2 11,11 3,20" fill="none" stroke="#fff" stroke-width="3"/></svg>
  <div class="hero-copy">
    <h1>NOLVIK IMAGING CENTER</h1>
    <p>The Nolvik Imaging Center is the most advanced free-standing diagnostic imaging center in Florida. Our board certified radiologists and caring staff deliver fast, accurate results, and we are proud to be the first imaging center in the area to offer a 3.0T MRI.</p>
    <span class="btn">MAKE AN APPOINTMENT</span>
  </div>
</section>

<section class="why">
  <div class="wrap">
    <h2 class="section-title">WHY WOULD YOU SEND YOUR PATIENTS ANYWHERE ELSE?</h2>
    <p class="lead">The Nolvik Imaging Center is the most advanced free-standing diagnostic imaging center in Florida. Our fully renovated facility offers the latest RO equipment, and our Nolvik Center team has served referring physicians for years. Every study is read by board certified radiologists using the newest software, with reports delivered quickly to you.</p>
    <div class="cards">
      <article class="card">
        <div class="card-img" role="img" aria-label="3.0T MRI scanner in a bright room" style="background:linear-gradient(135deg,#e7ecef,#b9c4cc)"></div>
        <h3>3.0 T QUILLMARK TN480 MRI</h3>
        <p>Sharp images and faster exams with our wide bore, high field magnet.</p>
        <span class="read-more">READ MORE »</span>
      </article>
      <article class="card">
        <div class="card-img" role="img" aria-label="128 slice PET/CT scanner" style="background:linear-gradient(135deg,#f1f3f4,#c7ced3)"></div>
        <h3>128 SLICE QUILLMARK PET/CT</h3>
        <p>Low dose scans with precise detail for cancer and cardiac studies.</p>
        <span class="read-more">READ MORE »</span>
      </article>
      <article class="card">
        <div class="card-img" role="img" aria-label="Technologist performing an ultrasound on a patient" style="background:linear-gradient(135deg,#dfe4e8,#9fb0bd)"></div>
        <h3>HIGH-RESOLUTION VAREN T4 ULTRASOUND MACHINE</h3>
        <p>Clear, real time imaging for abdominal and vascular exams.</p>
        <span class="read-more">READ MORE »</span>
      </article>
      <article class="card">
        <div class="card-img" role="img" aria-label="Patient on a bone density scanner" style="background:linear-gradient(135deg,#e9edf0,#b3bfc8)"></div>
        <h3>CT BONE DENSITY</h3>
        <p>Quick, accurate bone density testing with minimal exposure.</p>
        <span class="read-more">READ MORE »</span>
      </article>
    </div>
  </div>
</section>

<section class="divisions">
  <div class="wrap">
    <article class="division clinical">
      <div class="division-band"><span class="dot"></span><span>Nolvik Imaging Center</span></div>
      <div class="division-body">
        <h2>OUR CLINICAL NOLVIK CENTER DIVISION</h2>
        <p>The Nolvik Center is the most advanced free-standing diagnostic imaging center in Florida, serving physicians who refer patients for MRI, CT, PET and ultrasound.</p>
        <span class="read-more">READ MORE »</span>
      </div>
    </article>
    <article class="division wellspire">
      <div class="division-band"><span class="dot"></span><span>Wellspire</span></div>
      <div class="division-body">
        <h2>OUR WELLSPIRE DIVISION</h2>
        <p>The Wellspire full body scan is a single noninvasive exam of your body using the latest technology, MRI, CT and blood tests to catch problems early.</p>
        <span class="read-more">READ MORE »</span>
      </div>
    </article>
  </div>
</section>

<section class="feature">
  <div class="wrap">
    <h2 class="section-title">WELLSPIRE</h2>
    <div class="feature-row">
      <div class="feature-text">
        <p>Why wait until you are sick to find out about a serious health problem? Catch it when it is early and easily treated. Know now.</p>
        <p>Be proactive about your health! The Wellspire full body scan is a single noninvasive scan of your body using the latest technology, MRI, CT and blood tests to seek out and find the earliest signs of disease. Each full body scan includes a written report, a CD with all the images, and results reviewed in detail with a radiologist who will answer your questions and help you plan your next steps.</p>
      </div>
      <div class="feature-img" role="img" aria-label="Radiologist reviewing full body MRI images on a screen"></div>
    </div>
  </div>
</section>

<footer class="site-footer">
  <div class="wrap footer-cols">
    <div class="footer-col">
      <h4>About Us</h4>
      <p>The Nolvik Center is the most advanced free-standing diagnostic imaging center in Florida.</p>
      <p>The first outpatient facility to offer MRI in Florida, the Nolvik Center.</p>
    </div>
    <div class="footer-col">
      <h4>Schedule</h4>
      <table class="hours">
        <tr><td>Mon - Fri</td><td>8:00 am to 8:00 pm</td></tr>
        <tr><td>Sat</td><td>8:00 am to 4:00 pm</td></tr>
        <tr><td>Sun</td><td>Closed</td></tr>
        <tr><td colspan="2">After hours appointments available</td></tr>
      </table>
    </div>
    <div class="footer-col">
      <h4>Subscribe Our Newsletter</h4>
      <p>Register your email to get news from us.</p>
      <div class="field">Email address</div>
      <span class="btn">SIGN UP</span>
    </div>
    <div class="footer-col">
      <h4>Contact Us</h4>
      <div class="contact-line">
        <svg width="10" height="10" viewBox="0 0 10 10"><path d="M2 1 L4 1 L5 3.5 L3.8 4.5 Q4.8 6.2 5.5 6.2 L6.5 5 L9 6 L9 8 Q9 9 8 9 Q1 8.5 1 2 Q1 1 2 1Z" fill="#d0d0d0"/></svg>
        <span>(555) 018-4420</span>
      </div>
      <div class="contact-line">
        <svg width="10" height="8" viewBox="0 0 10 8"><rect x="0.5" y="0.5" width="9" height="7" fill="none" stroke="#d0d0d0"/><polyline points="0.5,0.5 5,4.5 9.5,0.5" fill="none" stroke="#d0d0d0"/></svg>
        <span>info@nolvikimaging.example</span>
      </div>
      <div class="social"><i></i><i></i><i></i></div>
    </div>
  </div>
  <div class="footer-bottom">
    <div class="wrap">
      <p>Home | About | Exams | Wellspire | Insurance | Schedule | Contact</p>
      <p>Nolvik Imaging Center © 2024. All rights reserved.</p>
    </div>
  </div>
</footer>

</body>
</html>
```